Quote Cards With TK May 2025 for Instagram

I would like to put these quotes over one of the pictures attached; Instagram (new size: 4:5 (1080 x 1350 pixels) One Quote per picture, and I want the quote to be bold or easy to read as well. I provided a few reference graphics that I really like as examples below. In very small letters at the bottom add @TKBarlowOnline

All of the pictures are attached; you can pick any photo and add one quote to it; but no stock photography

```html
<!DOCTYPE html>
<html lang="en">
<head>
<meta charset="UTF-8">
<title>Quote Card – TK</title>
<link href="https://fonts.googleapis.com/css2?family=Bebas+Neue&display=swap" rel="stylesheet">
<style>
  :root {
    --sky-top: #2c2b30;
    --sky-mid: #6e4a74;
    --glow: #e3a6d6;
    --mauve: #9a6a98;
    --foliage: #4f5a38;
    --band: rgba(8, 6, 10, 0.55);
    --text: #ffffff;
    --outfit: #1a1619;
  }
  html, body {
    margin: 0;
    padding: 0;
    width: 960px;
    height: 1200px;
    overflow: hidden;
    background: #000;
  }
  .card {
    position: relative;
    width: 960px;
    height: 1200px;
    overflow: hidden;
    font-family: "Bebas Neue", "Oswald", sans-serif;
    color: var(--text);
  }
  .backdrop {
    position: absolute;
    inset: 0;
    background:
      radial-gradient(ellipse 520px 560px at 800px 1020px, var(--foliage) 0%, rgba(79,90,56,0) 75%),
      linear-gradient(180deg, var(--sky-top) 0%, #4a3a52 28%, var(--sky-mid) 52%, #6a4a66 70%, #464236 100%);
  }
  .portrait {
    position: absolute;
    left: 0;
    top: 140px;
    width: 430px;
    height: 1060px;
    border-radius: 190px 210px 0 0;
    background:
      radial-gradient(ellipse 260px 360px at 300px 600px, var(--glow) 0%, rgba(227,166,214,0) 70%),
      radial-gradient(ellipse 200px 420px at 190px 720px, rgba(26,22,25,0.85) 0%, rgba(26,22,25,0) 80%),
      linear-gradient(180deg, #3a2a38 0%, var(--mauve) 40%, #8a5c86 62%, #3a2a36 100%);
  }
  .text-band {
    position: absolute;
    top: 0;
    left: 397px;
    width: 495px;
    height: 1200px;
    background: var(--band);
  }
  .quote {
    position: absolute;
    right: 98px;
    margin: 0;
    text-align: right;
    font-weight: 400;
    text-transform: uppercase;
  }
  .quote-headline {
    top: 146px;
    font-size: 78px;
    line-height: 78px;
    letter-spacing: -0.5px;
  }
  .quote-promise {
    top: 546px;
    font-size: 78px;
    line-height: 78px;
    letter-spacing: -0.5px;
  }
  .quote-cta {
    top: 664px;
    font-size: 70px;
    line-height: 67px;
    letter-spacing: -0.5px;
  }
  .handle {
    position: absolute;
    left: 628px;
    top: 1107px;
    margin: 0;
    font-size: 31px;
    line-height: 31px;
    letter-spacing: -0.4px;
    text-transform: uppercase;
  }
</style>
</head>
<body>
  <main class="card">
    <div class="backdrop" role="img" aria-label="Mountain landscape at dusk with a soft purple sky and green treetops"></div>
    <div class="portrait" role="img" aria-label="Woman in a sheer striped black top and black high-waist pants, posing with hands raised against a pink glow"></div>
    <div class="text-band"></div>

    <h1 class="quote quote-headline">This is the secret<br>women over 40<br>are using<br>to get snatched</h1>
    <p class="quote quote-promise">Without starving</p>
    <p class="quote quote-cta">Comment skinny to<br>get the exact plan.</p>

    <p class="handle">@TKBarlowOnline</p>
  </main>
</body>
</html>
```